New Property management company business cards

Looking for a new business card, to reflect new younger ownership
Card should be clean, simple and professional but with a modern layout that is conveys our new logo and business model

Key aspects of the business:

Property Management
Facility Maintenance
Project Management
Tenant Improvements

Mailing Address:
PO BOX 7186
Modesto CA, 95353

Phone: 209-614-8837
Direct: 209-614-8831

Doyle Farrant
President

Target Market(s)

Commercial property owners

Industry/Entity Type

Real Estate property management

Contact Information for Business Card

Open to all designs but lean toward vertical layouts

Requirements
Must have
• Logo and space to customize name and contact info

```html
<!DOCTYPE html>
<html lang="en">
<head>
<meta charset="utf-8">
<title>Valmora Property Management – Business Cards</title>
<link href="https://fonts.googleapis.com/css2?family=Lexend:wght@300;400;600&display=swap" rel="stylesheet">
<style>
  :root {
    --stage: #d9d9d9;
    --paper: #ffffff;
    --navy: #1d1e2e;
    --teal: #38bfae;
    --ink: #22232f;
  }
  * { margin: 0; padding: 0; box-sizing: border-box; }
  html, body { width: 1200px; height: 1200px; overflow: hidden; }
  body {
    background: var(--stage);
    font-family: "Lexend", sans-serif;
    color: var(--ink);
    position: relative;
  }
  .card {
    position: absolute;
    top: 240px;
    width: 400px;
    height: 700px;
    background: var(--paper);
    overflow: hidden;
  }
  .card--back { left: 150px; }
  .card--front { left: 650px; }

  /* Back side */
  .back-brand {
    position: absolute;
    left: 200px;
    top: 250px;
    transform: translate(-50%, -50%) rotate(-90deg);
    display: flex;
    align-items: center;
    gap: 22px;
    white-space: nowrap;
  }
  .brand-square {
    width: 34px;
    height: 34px;
    background: var(--teal);
    flex: none;
  }
  .brand-text { display: flex; flex-direction: column; }
  .brand-name {
    font-weight: 600;
    font-size: 46px;
    letter-spacing: 7px;
    line-height: 1;
    color: var(--navy);
  }
  .brand-tagline {
    font-weight: 400;
    font-size: 11px;
    letter-spacing: 7.2px;
    margin-top: 8px;
    color: var(--navy);
  }
  .services {
    position: absolute;
    left: 0; right: 0;
    bottom: 90px;
    list-style: none;
    text-align: center;
    font-size: 23px;
    font-weight: 400;
    line-height: 1.5;
    color: var(--navy);
  }

  /* Front side */
  .front-band {
    position: absolute;
    top: 0; left: 0; right: 0;
    height: 300px;
    background: var(--navy);
  }
  .front-brand {
    position: absolute;
    top: 110px;
    left: 0; right: 0;
    text-align: center;
    color: var(--paper);
  }
  .front-brand .brand-name { color: var(--paper); font-size: 44px; }
  .front-brand .brand-tagline { color: var(--paper); font-size: 11px; letter-spacing: 6.4px; margin-top: 10px; }
  .front-brand .brand-square {
    margin: 0 auto 26px;
    width: 26px; height: 26px;
  }
  .person {
    position: absolute;
    top: 350px;
    left: 0; right: 0;
    text-align: center;
  }
  .person-name {
    font-weight: 600;
    font-size: 33px;
    letter-spacing: 1px;
    color: var(--teal);
    text-transform: uppercase;
  }
  .person-role {
    font-weight: 400;
    font-size: 25px;
    margin-top: 2px;
    color: var(--ink);
  }
  .contact-icons {
    display: flex;
    justify-content: center;
    gap: 16px;
    margin-top: 26px;
  }
  .contact-icons svg { width: 34px; height: 34px; }
  .contact-list {
    list-style: none;
    margin-top: 18px;
    font-size: 24px;
    line-height: 1.32;
    font-weight: 400;
    color: var(--ink);
  }
</style>
</head>
<body>

  <section class="card card--back" aria-label="Business card, back">
    <div class="back-brand">
      <span class="brand-square"></span>
      <div class="brand-text">
        <span class="brand-name">VALMORA</span>
        <span class="brand-tagline">PROPERTY MANAGEMENT</span>
      </div>
    </div>
    <ul class="services">
      <li>Property Management</li>
      <li>Facility Maintenance</li>
      <li>Project Management</li>
      <li>Tenant Improvements</li>
    </ul>
  </section>

  <section class="card card--front" aria-label="Business card, front">
    <div class="front-band"></div>
    <div class="front-brand">
      <div class="brand-square"></div>
      <div class="brand-name">VALMORA</div>
      <div class="brand-tagline">PROPERTY MANAGEMENT</div>
    </div>

    <div class="person">
      <h1 class="person-name">Doyle Farrant</h1>
      <p class="person-role">President</p>

      <div class="contact-icons">
        <svg viewBox="0 0 34 34" aria-label="Phone">
          <circle cx="17" cy="17" r="17" fill="var(--teal)"/>
          <path d="M12 9c1 0 2 2.5 2.5 3.5.3.8-1.2 1.6-1 2.4.6 2 2.6 4 4.6 4.6.8.2 1.6-1.3 2.4-1 1 .5 3.5 1.5 3.5 2.5 0 1.5-1.8 3-3.5 3C14 24 10 20 10 13.5 10 11 11 9 12 9z" fill="#fff"/>
        </svg>
        <svg viewBox="0 0 34 34" aria-label="Mobile">
          <circle cx="17" cy="17" r="17" fill="var(--teal)"/>
          <rect x="12" y="8" width="10" height="18" rx="1.6" fill="none" stroke="#fff" stroke-width="2"/>
          <circle cx="17" cy="23" r="1" fill="#fff"/>
        </svg>
        <svg viewBox="0 0 34 34" aria-label="Email">
          <circle cx="17" cy="17" r="17" fill="var(--teal)"/>
          <rect x="9" y="11" width="16" height="12" rx="1" fill="#fff"/>
          <path d="M9.5 11.5 17 18l7.5-6.5" fill="none" stroke="var(--teal)" stroke-width="1.6"/>
        </svg>
        <svg viewBox="0 0 34 34" aria-label="Website">
          <circle cx="17" cy="17" r="17" fill="var(--teal)"/>
          <circle cx="17" cy="17" r="8" fill="none" stroke="#fff" stroke-width="2"/>
          <path d="M9 17h16M17 9c-3 3-3 13 0 16M17 9c3 3 3 13 0 16" fill="none" stroke="#fff" stroke-width="1.5"/>
        </svg>
      </div>

      <ul class="contact-list">
        <li>209-614-8837</li>
        <li>209-614-8831</li>
        <li>doyle@valmorapm.com</li>
        <li>www.valmorapm.com</li>
      </ul>
    </div>
  </section>

</body>
</html>
```